Ironbark Hire

Ironbark hire (Business Name) is a rental equipment provider for the civil and mining industry's. We have a range of equipment which is ready for any project as big or little as it maybe

Equipment list
Water carts
Excavators
skid steers
Front end loaders
Vehicles
Pressure washers
Plant trailers
Trailers
Machine attachments - 4in1 buckets for skid steers, rock breakers,

We have a solid base within port Hedland supplying some of the largest company's within the Pilbara.
We have a coemptive edge with our pricing Strategy have some unique options we can provide for company's.
We have a low cost operation with first class assets, we can do this by partnering with a local Indigenous owned and operated company KRV contracting, we assist each other with yard sharing, labour and equipment. This is a win win for both business and also establishes employment options for young Indigenous

The Broucher is to explain to anyone, what we do and what the differences are with our company. It will need to cover of equipment we can supply and why we are a good option for a company's projects.
The design is to establish a professional look for our company to grow within a large cooperate industry. The design can encompass our company colours and logo.

Industry/Entity Type

Mining

```html
<!DOCTYPE html>
<html lang="en">
<head>
<meta charset="utf-8">
<title>Ironbark Hire – Presentation Folder</title>
<link href="https://fonts.googleapis.com/css2?family=Ubuntu:wght@400;700&display=swap" rel="stylesheet">
<style>
  :root {
    --backdrop: #d9d9d9;
    --paper: #f7f7f7;
    --ink: #2b2b2b;
    --ink-soft: #3a3a3a;
    --brand-yellow: #f2c21b;
    --shadow: rgba(0,0,0,0.22);
  }
  html, body {
    margin: 0;
    padding: 0;
    width: 1200px;
    height: 847px;
    overflow: hidden;
    background: var(--backdrop);
    font-family: "Ubuntu", sans-serif;
    color: var(--ink);
  }
  .spread {
    position: absolute;
    left: 180px;
    top: 126px;
    width: 840px;
    height: 594px;
    display: flex;
    box-shadow: 0 14px 30px var(--shadow);
  }
  .panel {
    position: relative;
    width: 420px;
    height: 594px;
    background: var(--paper);
    overflow: hidden;
  }
  .panel--back { border-right: 1px solid #e2e2e2; }
  .panel-art {
    position: absolute;
    inset: 0;
    width: 420px;
    height: 594px;
  }
  .brand {
    position: absolute;
    display: flex;
    align-items: center;
    gap: 8px;
  }
  .brand-dot {
    width: 14px;
    height: 14px;
    border-radius: 50%;
    background: var(--brand-yellow);
  }
  .brand-name {
    font-weight: 700;
    color: var(--ink);
    text-transform: uppercase;
    letter-spacing: 0.5px;
    white-space: nowrap;
  }
  .brand-tagline {
    position: absolute;
    font-size: 8px;
    color: var(--ink-soft);
    white-space: nowrap;
  }
  .panel--back .brand { left: 60px; top: 344px; }
  .panel--back .brand-name { font-size: 18px; }
  .panel--back .brand-tagline { left: 82px; top: 370px; font-size: 6.5px; }
  .panel--front .brand { left: 110px; top: 72px; }
  .panel--front .brand-name { font-size: 26px; }
  .panel--front .brand-tagline { left: 150px; top: 108px; font-size: 8.5px; }
  .contact {
    position: absolute;
    left: 62px;
    top: 408px;
    font-size: 11px;
    line-height: 1.35;
    color: var(--ink-soft);
  }
  .contact p { margin: 0 0 12px; }
  .contact .contact-group p { margin: 0; }
  .contact .contact-group { margin-bottom: 12px; }
</style>
</head>
<body>
  <main class="spread">
    <section class="panel panel--back">
      <svg class="panel-art" viewBox="0 0 420 594" aria-hidden="false">
        <defs>
          <linearGradient id="loader-tones" x1="0" y1="0" x2="1" y2="0">
            <stop offset="0" stop-color="#5a4630"/>
            <stop offset="0.5" stop-color="#c9a41c"/>
            <stop offset="1" stop-color="#6b5a44"/>
          </linearGradient>
        </defs>
        <polygon role="img" aria-label="Photo of a yellow front end loader on a dirt site"
                 points="175,300 420,178 420,290 260,296" fill="url(#loader-tones)"/>
      </svg>

      <div class="brand">
        <span class="brand-dot"></span>
        <span class="brand-name">Ironbark Hire</span>
      </div>
      <span class="brand-tagline">Civil + Mining Plant Hire</span>

      <div class="contact">
        <p>Contact Us:</p>
        <p>Address Company</p>
        <div class="contact-group">
          <p>Phone: xxx.xxx.xxx</p>
          <p>Fax: xxx.xxx.xxx</p>
        </div>
        <div class="contact-group">
          <p>Email: info@ironbarkhire.com</p>
          <p>Website: www.ironbarkhire.com</p>
        </div>
      </div>
    </section>

    <section class="panel panel--front">
      <div class="brand">
        <span class="brand-dot"></span>
        <span class="brand-name">Ironbark Hire</span>
      </div>
      <span class="brand-tagline">Civil + Mining Plant Hire</span>

      <svg class="panel-art" viewBox="0 0 420 594">
        <defs>
          <linearGradient id="dumptruck-tones" x1="0" y1="0" x2="0" y2="1">
            <stop offset="0" stop-color="#5b8fd0"/>
            <stop offset="0.55" stop-color="#b9cfe6"/>
            <stop offset="1" stop-color="#6a5640"/>
          </linearGradient>
          <linearGradient id="excavator-tones" x1="0" y1="0" x2="1" y2="1">
            <stop offset="0" stop-color="#3f78c8"/>
            <stop offset="0.5" stop-color="#d8b51e"/>
            <stop offset="1" stop-color="#7d6a50"/>
          </linearGradient>
          <linearGradient id="carrier-tones" x1="0" y1="0" x2="0" y2="1">
            <stop offset="0" stop-color="#6f9a3c"/>
            <stop offset="0.5" stop-color="#5c5c60"/>
            <stop offset="1" stop-color="#9a9a9c"/>
          </linearGradient>
        </defs>
        <polygon role="img" aria-label="Photo of a large mining dump truck under a blue sky"
                 points="20,140 420,198 330,236 40,246" fill="url(#dumptruck-tones)"/>
        <polygon role="img" aria-label="Photo of a yellow excavator arm and bucket against the sky"
                 points="52,258 420,206 420,372 82,366" fill="url(#excavator-tones)"/>
        <polygon role="img" aria-label="Photo of a car carrier truck loaded with vehicles on a highway"
                 points="88,384 420,330 420,594 110,594" fill="url(#carrier-tones)"/>
      </svg>
    </section>
  </main>
</body>
</html>
```